New shirt company looking for a fun and edgy online retail website design

We're a new company looking for a simple yet attractive website to sell shirts/tops to a mostly younger female audience. Our name is Tavi Shirt Co. and the PlanHerd logo is uploaded. We're thinking a home page, three separate pages for our shirt "collections", and a contact page/cart page for a grand total of 5 pages. We'd like the website to be coded, easy for the consumer to navigate/shop/checkout, and easy to link to various social media platforms and online websites. For colors, we're aiming for various blues, light grey, and maybe tan/khaki. Our goal is to launch with approximately 20-30 tops/shirts (or 7-10) per page. Please let us know if you have any questions and thank you for helping us! We are very excited to see what is created!

Target Market(s)

Female teens to early twenties

Coding

Coded - Design and coding required

Number of Pages Required

3 page

Font styles to use
Decorative
Script

Colors
cee9f5
85cae6
33a6d7
0393ce
cfdfed
85acd3

Requirements
Must have
• Online shopping/purchasing capabilities, dropdowns to select sizes for each item, easy to add/remove new or seasoned items.

```html
<!DOCTYPE html>
<html lang="en">
<head>
<meta charset="utf-8">
<title>Tavi Shirt Co. — Home</title>
<link href="https://fonts.googleapis.com/css2?family=Oswald:wght@300;500;700&family=PT+Serif:ital,wght@0,400;0,700;1,400&family=Poppins:wght@400;500;600&display=swap" rel="stylesheet">
<style>
:root{
  --sky:#8dcbea;
  --sky-deep:#6fb8de;
  --navy:#13294b;
  --blue:#0a8fd0;
  --blue-dark:#0678b3;
  --ink:#1b2233;
  --muted:#8a93a3;
  --tab-muted:#a9c3da;
  --line:#dfe6ee;
  --card:#f4f5f7;
  --white:#ffffff;
}
*{box-sizing:border-box;margin:0;padding:0}
html,body{width:1200px;height:3781px;overflow:hidden;background:var(--white)}
body{position:relative;font-family:"Poppins",sans-serif;color:var(--ink)}
.abs{position:absolute}
.serif{font-family:"PT Serif",serif}
.display{font-family:"Oswald",sans-serif}
.btn{position:absolute;background:var(--blue);color:var(--white);font-family:"PT Serif",serif;font-size:15px;display:flex;align-items:center;justify-content:center;letter-spacing:.3px}
.photo{position:absolute}

/* header */
.hero{left:0;top:0;width:1200px;height:713px;background:var(--sky)}
.hero-band{left:0;top:487px;width:1200px;height:226px;background:var(--navy)}
.logo{left:161px;top:18px;height:51px;display:flex;align-items:center;gap:10px;color:var(--blue-dark);font-family:"PT Serif",serif;font-weight:700;font-size:24px}
.logo .mark{width:18px;height:18px;border:2px solid var(--blue-dark)}
.nav{top:28px;left:623px;display:flex;gap:0;font-size:12px;color:var(--ink)}
.nav a{position:absolute;white-space:nowrap;text-decoration:none;color:var(--ink)}
.nav a.active{color:var(--blue-dark);font-weight:600}
.nav a.active::after{content:"";position:absolute;left:0;right:0;bottom:-6px;height:2px;background:var(--blue-dark)}
.hero-photo{left:587px;top:95px;width:455px;height:618px;background:linear-gradient(180deg,#3a2c28 0%,#e7e4e0 45%,#2a2a2e 100%);border-radius:140px 140px 0 0}
.hero-kicker{left:194px;top:232px;font-family:"Oswald",sans-serif;font-weight:300;font-size:44px;color:var(--navy)}
.hero-title{left:192px;top:280px;font-family:"Oswald",sans-serif;font-weight:700;font-size:62px;color:var(--navy);letter-spacing:.5px;line-height:1}
.hero-sub{left:194px;top:358px;font-family:"Oswald",sans-serif;font-weight:300;font-size:16px;color:var(--navy)}
.hero-sub b{font-family:"PT Serif",serif;font-weight:700;color:var(--white)}
.dots{left:193px;top:657px;display:flex;gap:5px}
.dots span{width:12px;height:12px;border:1.5px solid var(--white);border-radius:50%}
.dots span.on{background:var(--blue);border-color:var(--blue)}

/* tabs */
.tabs{left:0;width:1200px;top:797px;display:flex;justify-content:center;gap:0;font-family:"PT Serif",serif;font-size:22px}
.tabs span{color:var(--tab-muted);padding:0 24px;border-left:1px solid var(--line)}
.tabs span:first-child{border:0;color:var(--blue-dark)}
.divider{height:1px;background:var(--line)}
.xx{font-size:11px;color:var(--blue);letter-spacing:1px;background:var(--white);padding:0 6px}

/* product cards */
.card{position:absolute;top:915px;width:203px;height:336px;border:1px solid var(--line);background:var(--white)}
.card .img{height:247px;background:var(--card);display:flex;align-items:center;justify-content:center}
.card .name{text-align:center;font-family:"PT Serif",serif;font-size:18px;margin-top:26px}
.card .price{text-align:center;font-size:12px;color:var(--blue-dark);margin-top:2px}
.arrow{position:absolute;top:1066px;width:33px;height:33px;border:1.5px solid var(--ink);display:flex;align-items:center;justify-content:center}

/* promos */
.promo{position:absolute;top:1328px;height:412px;overflow:hidden}

/* collection grid */
.tile{position:absolute;width:270px;height:261px;display:flex;align-items:center;justify-content:center}
.tile .label{font-family:"Oswald",sans-serif;font-size:29px;color:var(--white);text-shadow:0 1px 3px rgba(0,0,0,.35)}

/* features */
.feature{position:absolute;top:2910px;width:240px;text-align:center}
.feature h3{font-family:"PT Serif",serif;font-weight:400;font-size:18px;margin-top:22px;color:var(--ink)}
.feature p{font-size:10px;color:var(--muted);margin-top:2px}

/* footer */
.col{position:absolute;top:3420px}
.col h4{font-family:"PT Serif",serif;font-weight:700;font-size:13px;letter-spacing:.2px;margin-bottom:22px}
.col li{list-style:none;font-size:10.5px;color:#59606d;height:22.6px;position:relative;padding-left:16px}
.col li::before{content:"";position:absolute;left:0;top:6px;width:5px;height:5px;border-radius:50%;background:var(--blue)}
.contact-row{display:flex;gap:12px;font-size:10.5px;color:#59606d;margin-bottom:14px;align-items:flex-start}
.pay{display:flex;gap:3px;margin-top:6px}
.pay span{width:40px;height:22px;border-radius:2px}
.social{left:525px;top:3684px;display:flex;gap:7px}
.social span{width:32px;height:32px;border-radius:50%;border:2px solid var(--blue-dark)}
.social span.on{background:var(--blue-dark)}
</style>
</head>
<body>

<!-- Hero -->
<section class="abs hero"></section>
<div class="abs hero-band"></div>
<div class="photo hero-photo" role="img" aria-label="Photo of a young woman in a black leather jacket and white cropped printed top, arms raised"></div>

<div class="abs logo"><span class="mark"></span>Tavi Shirt Co.</div>
<nav class="abs nav" style="left:0;top:28px;width:1200px">
  <a class="active" href="#" style="left:623px">Home</a>
  <a href="#" style="left:685px">Collections</a>
  <a href="#" style="left:773px">Shop</a>
  <a href="#" style="left:829px">Contact</a>
  <a href="#" style="left:898px">Check Out</a>
</nav>
<svg class="abs" style="left:986px;top:29px" width="16" height="16" viewBox="0 0 16 16" aria-label="Search"><circle cx="6.5" cy="6.5" r="5" fill="none" stroke="#1b2233" stroke-width="1.6"/><line x1="10.2" y1="10.2" x2="14.5" y2="14.5" stroke="#1b2233" stroke-width="1.6"/></svg>
<svg class="abs" style="left:1014px;top:25px" width="26" height="22" viewBox="0 0 26 22" aria-label="Cart"><path d="M1 5h3l2.4 9h9.6l2.2-7H6" fill="none" stroke="#1b2233" stroke-width="1.6"/><circle cx="8" cy="18" r="1.6" fill="#1b2233"/><circle cx="15" cy="18" r="1.6" fill="#1b2233"/><circle cx="20" cy="5" r="5" fill="#0a8fd0"/><text x="20" y="7.5" font-size="7" fill="#fff" text-anchor="middle" font-family="Poppins">0</text></svg>

<div class="abs hero-kicker">DREAM GIRLS</div>
<h1 class="abs hero-title">FASHION STREET</h1>
<div class="abs hero-sub">EVERYTHING YOU NEED <b>COLLECTION 2020</b></div>
<a class="btn" style="left:194px;top:402px;width:231px;height:44px">SHOP THE COLLECTION</a>
<div class="abs dots"><span></span><span class="on"></span><span></span><span></span><span></span></div>

<!-- Tabs -->
<div class="abs tabs"><span>FEATURED</span><span>NEW ARRIVAL</span><span>SPECIALS</span></div>
<div class="abs divider" style="left:345px;top:852px;width:510px"></div>
<div class="abs" style="left:0;width:1200px;top:844px;text-align:center"><span class="xx">xxxx</span></div>

<!-- Featured products -->
<div class="arrow" style="left:91px"><svg width="12" height="14" viewBox="0 0 12 14"><path d="M8 1L2 7l6 6" fill="none" stroke="#1b2233" stroke-width="1.6"/></svg></div>
<div class="arrow" style="left:1077px"><svg width="12" height="14" viewBox="0 0 12 14"><path d="M4 1l6 6-6 6" fill="none" stroke="#1b2233" stroke-width="1.6"/></svg></div>

<article class="card" style="left:161px">
  <div class="img"><div role="img" aria-label="White button-up shirt" style="width:110px;height:200px;background:linear-gradient(180deg,#ffffff,#e6e8ec);border-radius:20px 20px 6px 6px"></div></div>
  <div class="name">Tavi Shirt</div><div class="price">$200.00</div>
</article>
<article class="card" style="left:386px">
  <div class="img" style="height:187px;align-items:flex-end;overflow:hidden"><div role="img" aria-label="Pale blue blouse" style="width:130px;height:170px;background:linear-gradient(180deg,#dfe8f3,#c4d5ea);border-radius:20px 20px 0 0"></div></div>
  <a class="btn" style="left:25px;top:64px;width:150px;height:33px;font-size:11px">&#9776;&nbsp; SELECT OPTIONS</a>
  <div class="abs" style="left:0;top:112px;width:201px;text-align:center;font-size:10.5px;color:#4a5160">QuickView &nbsp;|&nbsp; Whishlist</div>
  <div class="name" style="margin-top:28px">Tavi Top</div><div class="price">$200.00</div>
  <div class="abs" style="left:46px;top:278px;width:106px;height:28px;border:1px solid var(--line);display:flex;font-size:10.5px">
    <span style="background:#e6eaef;width:42px;display:flex;align-items:center;justify-content:center">Size :</span>
    <span style="flex:1;display:flex;align-items:center;justify-content:space-between;padding:0 8px">m <svg width="10" height="6"><path d="M1 1l4 4 4-4" fill="none" stroke="#0a8fd0" stroke-width="1.3"/></svg></span>
  </div>
</article>
<article class="card" style="left:610px">
  <div class="img"><div role="img" aria-label="Red sweatshirt" style="width:130px;height:130px;background:#ef3f4c;border-radius:30px 30px 8px 8px"></div></div>
  <div class="name">Tavi Shirt</div><div class="price">$200.00</div>
</article>
<article class="card" style="left:836px">
  <div class="img"><div role="img" aria-label="Blue denim jacket" style="width:140px;height:150px;background:linear-gradient(180deg,#5a86ba,#2f5d92);border-radius:20px 20px 6px 6px"></div></div>
  <div class="name">Tavi Shirt</div><div class="price">$200.00</div>
</article>

<!-- Promo banners -->
<section class="promo" style="left:161px;width:432px;background:var(--navy)">
  <div class="photo" role="img" aria-label="Photo of a smiling young woman in a plaid tied top and white jeans" style="left:170px;top:12px;width:262px;height:400px;background:linear-gradient(180deg,#4a3030 0%,#7b4a5a 40%,#e9e7ea 75%,#ffffff 100%);opacity:.85"></div>
  <div class="abs serif" style="left:27px;top:174px;font-style:italic;font-size:25px;color:var(--sky-deep)">Hurry Up !</div>
  <div class="abs display" style="left:26px;top:204px;font-weight:700;font-size:64px;color:var(--white);line-height:1">NEW WOMEN</div>
  <div class="abs display" style="left:26px;top:282px;font-weight:400;font-size:36px;color:var(--white)">COLLECTION</div>
  <a class="btn" style="left:28px;top:340px;width:127px;height:38px">SHOP NOW</a>
</section>
<section class="promo" style="left:607px;width:432px;background:linear-gradient(90deg,#2b2825,#564a40 55%,#8a7a68)">
  <div class="photo" role="img" aria-label="Photo of a woman in a black turtleneck and checked coat" style="left:140px;top:0;width:292px;height:412px;background:linear-gradient(180deg,#3a332e,#6f6256 60%,#9b8b78);opacity:.7"></div>
  <div class="abs" style="left:38px;top:46px;width:76px;height:76px;border-radius:50%;background:var(--blue);border:3px solid var(--white);box-shadow:0 0 0 3px var(--blue);display:flex;align-items:center;justify-content:center;font-family:'PT Serif',serif;font-style:italic;font-weight:700;font-size:21px;color:var(--white)">$280</div>
  <div class="abs display" style="left:0;width:432px;text-align:center;top:200px;font-weight:700;font-size:66px;color:var(--white);line-height:1">GO OUT IN</div>
  <div class="abs display" style="left:0;width:432px;text-align:center;top:270px;font-size:36px;color:var(--white)">STYLE</div>
  <a class="btn" style="left:157px;top:328px;width:127px;height:38px">SHOP NOW</a>
</section>

<!-- Our collection -->
<h2 class="abs serif" style="left:0;width:1200px;text-align:center;top:1810px;font-weight:400;font-size:41px;color:var(--navy)">OUR COLLECTION</h2>
<div class="abs divider" style="left:345px;top:1884px;width:510px"></div>
<div class="abs" style="left:0;width:1200px;top:1876px;text-align:center"><span class="xx">xxxx</span></div>

<div class="tile" style="left:173px;top:1935px;background:#d8d3cd" role="img" aria-label="Olive sleeveless top with lace shoulders"><div style="position:absolute;width:110px;height:230px;background:#746c5a;border-radius:30px 30px 10px 10px"></div><span class="label" style="position:relative">Tavi Top</span></div>
<div class="tile" style="left:465px;top:1935px;background:#ddd6d0" role="img" aria-label="White striped shirt on a hanger"><div style="position:absolute;width:150px;height:230px;background:#f7f7f5;border-radius:30px 30px 6px 6px"></div><span class="label" style="position:relative;color:var(--navy);text-shadow:none;top:-24px">Tavi Shirt</span><a class="btn" style="left:75px;top:144px;width:127px;height:36px">SHOP NOW</a></div>
<div class="tile" style="left:757px;top:1935px;background:#cfdfed" role="img" aria-label="Navy striped blouse"><div style="position:absolute;width:140px;height:220px;background:#24305f;border-radius:30px 30px 6px 6px"></div><span class="label" style="position:relative">Tavi Shirt</span></div>

<div class="tile" style="left:173px;top:2220px;background:#dcdde1" role="img" aria-label="Cream knit sweater"><div style="position:absolute;width:180px;height:220px;background:#f3ead6;border-radius:30px 30px 16px 16px"></div><span class="label" style="position:relative">Tavi Top</span></div>
<div class="tile" style="left:465px;top:2220px;background:#f1e7e8" role="img" aria-label="Pink v-neck blouse"><div style="position:absolute;width:160px;height:200px;background:#eea7b2;border-radius:30px 30px 10px 10px"></div><span class="label" style="position:relative">Tavi Shirt</span></div>
<div class="tile" style="left:757px;top:2220px;background:#f1f1f1" role="img" aria-label="Black and white striped blouse"><div style="position:absolute;width:170px;height:220px;background:repeating-linear-gradient(90deg,#141b33 0 10px,#ffffff 10px 16px);border-radius:30px 30px 10px 10px"></div><span class="label" style="position:relative">Tavi Shirt</span></div>

<div class="tile" style="left:173px;top:2504px;background:#b9b9bb" role="img" aria-label="White top with floral embroidery"><div style="position:absolute;width:200px;height:200px;background:#ffffff;border-radius:30px 30px 10px 10px"></div><span class="label" style="position:relative">Tavi Top</span></div>
<div class="tile" style="left:465px;top:2504px;background:#eef0f3" role="img" aria-label="Light blue tie-front shirt"><div style="position:absolute;width:150px;height:230px;background:#a9c8e6;border-radius:30px 30px 10px 10px"></div><span class="label" style="position:relative">Tavi Top</span></div>
<div class="tile" style="left:757px;top:2504px;background:#dcd6ce" role="img" aria-label="Khaki belted top"><div style="position:absolute;width:180px;height:200px;background:#c3bda6;border-radius:30px 30px 10px 10px"></div><span class="label" style="position:relative">Tavi Top</span></div>

<a class="btn" style="left:484px;top:2799px;width:232px;height:40px">SHOP THE COLLECTION</a>

<!-- Features -->
<div class="feature" style="left:234px">
  <svg width="54" height="40" viewBox="0 0 54 40"><rect x="2" y="6" width="30" height="22" fill="#0a8fd0"/><path d="M32 13h10l8 8v7H32z" fill="#0a8fd0"/><circle cx="12" cy="32" r="5" fill="#fff" stroke="#0a8fd0" stroke-width="3"/><circle cx="42" cy="32" r="5" fill="#fff" stroke="#0a8fd0" stroke-width="3"/><path d="M10 17h14m-4-4 4 4-4 4" stroke="#fff" stroke-width="2" fill="none"/></svg>
  <h3>FREE Shippimg</h3><p>Lorem Ipsum Simple Text Print</p>
</div>
<div class="abs" style="left:478px;top:2920px;width:1px;height:98px;background:var(--line)"></div>
<div class="feature" style="left:480px">
  <svg width="44" height="40" viewBox="0 0 44 40"><path d="M6 14h26l-3 22H9z" fill="#0a8fd0"/><path d="M13 14a6 6 0 0 1 12 0" fill="none" stroke="#0a8fd0" stroke-width="2.5"/><circle cx="32" cy="28" r="8" fill="#fff" stroke="#0a8fd0" stroke-width="3"/></svg>
  <h3>Shopping Guide</h3><p>Lorem Ipsum Simple Text Print</p>
</div>
<div class="abs" style="left:725px;top:2920px;width:1px;height:98px;background:var(--line)"></div>
<div class="feature" style="left:731px">
  <svg width="40" height="44" viewBox="0 0 40 44"><path d="M20 2 36 10v14L20 32 4 24V10z" fill="#0a8fd0"/><path d="M8 30l12 8 12-8" fill="none" stroke="#0a8fd0" stroke-width="3"/><path d="M12 16l6 5 10-9" fill="none" stroke="#fff" stroke-width="2.5"/></svg>
  <h3>Return Guarantee</h3><p>Lorem Ipsum Simple Text Print</p>
</div>

<!-- Newsletter band -->
<section class="abs" style="left:0;top:3093px;width:398px;height:284px;background:linear-gradient(135deg,#4a3c3a,#2d4f9c 60%,#6b5a52)" role="img" aria-label="Photo of a young woman in a blue sweater and sunglasses">
  <div class="abs display" style="left:0;width:398px;text-align:center;top:122px;font-weight:700;font-size:42px;color:var(--white);text-shadow:0 2px 4px rgba(0,0,0,.4)">DREAM GIRLS</div>
</section>
<section class="abs" style="left:400px;top:3093px;width:400px;height:284px;background:var(--blue)">
  <div class="abs" style="left:4px;top:4px;right:4px;bottom:4px;border:1px solid rgba(255,255,255,.6)"></div>
  <h2 class="abs serif" style="left:0;width:400px;text-align:center;top:54px;font-weight:400;font-size:33px;color:var(--white)">NEWSLETTER</h2>
  <p class="abs" style="left:0;width:400px;text-align:center;top:100px;font-size:12.5px;color:var(--white)">Sign up Newsletter For Our Latest Update !</p>
  <div class="abs" style="left:53px;top:133px;width:294px;height:39px;background:var(--white);display:flex;align-items:center;justify-content:space-between;padding:0 12px;font-size:10px;color:var(--muted)">Enter Email *<svg width="14" height="10" viewBox="0 0 14 10"><rect x="1" y="1" width="12" height="8" fill="none" stroke="#0a8fd0" stroke-width="1.3"/><path d="M1 1l6 5 6-5" fill="none" stroke="#0a8fd0" stroke-width="1.3"/></svg></div>
  <a class="abs serif" style="left:137px;top:183px;width:126px;height:40px;border:1px solid var(--white);color:var(--white);font-size:15px;display:flex;align-items:center;justify-content:center">SUBSCRIBE</a>
</section>
<section class="abs" style="left:802px;top:3093px;width:398px;height:284px;background:linear-gradient(135deg,#9a8f85,#e9e6e2 55%,#8f8a86)" role="img" aria-label="Photo of a woman in a white shirt and sunglasses">
  <div class="abs display" style="left:0;width:398px;text-align:center;top:122px;font-weight:700;font-size:42px;color:var(--white);text-shadow:0 2px 4px rgba(0,0,0,.4)">BEST COLLECTION</div>
</section>

<!-- Footer -->
<footer>
  <div class="col" style="left:163px"><h4>INFORMATION</h4><ul><li>About Us</li><li>Customer Service</li><li>Search Terms</li><li>Privacy Policy</li><li>Advanced Search</li><li>Orders and Returns</li><li>Contact Us</li></ul></div>
  <div class="col" style="left:387px"><h4>CUSTOMER SERVICES</h4><ul><li>About Us</li><li>Faq</li><li>Collections</li><li>Blog</li><li>Contact Us</li></ul></div>
  <div class="col" style="left:613px"><h4>MY ACCOUNT</h4><ul><li>Sign In</li><li>View Cart</li><li>My Wishlist</li><li>FAQ</li></ul></div>
  <div class="col" style="left:838px"><h4>CONTACT US</h4>
    <div class="contact-row"><svg width="14" height="10" viewBox="0 0 14 10"><rect width="14" height="10" fill="#0a8fd0"/><path d="M0 0l7 5 7-5" fill="none" stroke="#fff" stroke-width="1.2"/></svg>hello@tavishirtco.com</div>
    <div class="contact-row" style="font-weight:600;color:var(--blue-dark);font-size:13px"><svg width="14" height="14" viewBox="0 0 14 14"><path d="M3 1l3 3-2 2c1 2 2 3 4 4l2-2 3 3-2 2C6 13 1 8 1 3z" fill="#0a8fd0"/></svg>123 456 7890</div>
    <div class="contact-row"><svg width="12" height="16" viewBox="0 0 12 16"><path d="M6 15S1 9 1 6a5 5 0 0 1 10 0c0 3-5 9-5 9z" fill="#0a8fd0"/><circle cx="6" cy="6" r="2" fill="#fff"/></svg><span>TaviShirtCo<br>101 ~ Lorem ipsum simple text</span></div>
    <div class="pay" aria-label="Accepted payment cards"><span style="background:#e9edf5"></span><span style="background:#f2a73b"></span><span style="background:#3b7cc4"></span><span style="background:#d9d9d9"></span></div>
  </div>
  <div class="abs divider" style="left:161px;top:3647px;width:878px"></div>
  <div class="abs social" aria-label="Social links"><span class="on"></span><span></span><span></span><span></span></div>
  <p class="abs" style="left:0;width:1200px;text-align:center;top:3727px;font-size:10px;color:#59606d">©Tavi Shirt Co.- 2020 All right reserved.</p>
</footer>

</body>
</html>
```